Stationery Design Project

KT7 Staffing requires letterhead and business card designs for a company based in London. Just like the name, we're a management resourcing company, providing resources to third party companies. You can see www.kt7staffing-example.com for ideas on existing colour schemes and design concepts that have been implimented and agreed to. Ultimately the design should broadcast professionalism, safety and the concept of growth.

Target Market(s)

Financial institutes; friendly societies (All UK based)

Industry/Entity Type

Safety

Requirements
Must have
• Files produced should be print ready; and the text in them editable (eg address, name etc)

```html
<!DOCTYPE html>
<html lang="en">
<head>
<meta charset="utf-8">
<title>KT7 Staffing — Stationery</title>
<link rel="stylesheet" href="https://fonts.googleapis.com/css2?family=Open+Sans:wght@400;600;700&display=swap">
<style>
  :root {
    --board: #2d2d2f;
    --board-edge: #3a3a3c;
    --paper: #ffffff;
    --teal: #1a9fb0;
    --teal-deep: #1e8f98;
    --sky: #7bbfdc;
    --ink-grey: #8a8a8a;
    --mist: #d6d6d6;
  }
  * { box-sizing: border-box; margin: 0; padding: 0; }
  html, body { width: 1200px; height: 1091px; overflow: hidden; }
  body {
    background: var(--board);
    font-family: "Open Sans", Arial, sans-serif;
    position: relative;
  }
  .board-frame {
    position: absolute; inset: 0;
    border: 2px solid var(--board-edge);
  }
  .letterhead {
    position: absolute; left: 98px; top: 76px;
    width: 649px; height: 917px;
    background: var(--paper);
  }
  .wordmark {
    position: absolute;
    display: flex; align-items: center; gap: 8px;
    font-weight: 700; color: var(--teal-deep);
    letter-spacing: 0.01em; white-space: nowrap;
  }
  .wordmark .mark-square { background: var(--sky); flex: none; }
  .letterhead .wordmark { left: 33px; top: 36px; font-size: 34px; }
  .letterhead .wordmark .mark-square { width: 28px; height: 28px; }
  .growth-corner {
    position: absolute;
    background: linear-gradient(135deg, rgba(123,191,220,0) 30%, rgba(123,191,220,0.35) 65%, rgba(26,159,176,0.45) 100%);
  }
  .letterhead .growth-corner { right: 0; bottom: 0; width: 193px; height: 246px; }
  .letterhead-footer {
    position: absolute; left: 51px; top: 875px;
    display: flex; gap: 71px;
    font-size: 12px; line-height: 15px; color: var(--ink-grey);
  }
  .letterhead-footer .col { width: 150px; white-space: nowrap; }
  .card {
    position: absolute; left: 801px;
    width: 276px; height: 157px; overflow: hidden;
  }
  .card-front { top: 74px; background: var(--teal); }
  .card-front .wordmark { left: 26px; top: 24px; font-size: 18px; color: var(--paper); gap: 6px; }
  .card-front .wordmark .mark-square { width: 14px; height: 14px; background: var(--paper); }
  .card-front .growth-corner {
    right: 0; bottom: 0; width: 92px; height: 112px;
    background: linear-gradient(135deg, rgba(255,255,255,0) 35%, rgba(255,255,255,0.3) 100%);
  }
  .card-back { top: 279px; background: var(--paper); }
  .card-back .holder { position: absolute; left: 19px; top: 16px; color: var(--ink-grey); }
  .holder .name { font-size: 9px; font-weight: 700; letter-spacing: 0.06em; line-height: 12px; }
  .holder .role { font-size: 7px; line-height: 9px; }
  .holder .contact { margin-top: 8px; font-size: 7px; line-height: 9px; }
  .card-back .wordmark { left: 19px; top: 88px; font-size: 14px; gap: 5px; }
  .card-back .wordmark .mark-square { width: 11px; height: 11px; }
  .card-back .growth-corner {
    right: 0; bottom: 0; width: 92px; height: 112px;
    background: linear-gradient(135deg, rgba(214,214,214,0) 35%, rgba(214,214,214,0.55) 100%);
  }
</style>
</head>
<body>
  <div class="board-frame"></div>

  <section class="letterhead">
    <div class="wordmark"><span class="mark-square"></span>KT7 Staffing</div>
    <div class="growth-corner" role="img" aria-label="Brand growth motif in teal and sky blue"></div>
    <footer class="letterhead-footer">
      <div class="col">(421) 555.0192<br>12 Harrow Lane London</div>
      <div class="col">media@kt7staffing-example.com<br>www.kt7staffing-example.com</div>
    </footer>
  </section>

  <section class="card card-front">
    <div class="wordmark"><span class="mark-square"></span>KT7 Staffing</div>
    <div class="growth-corner" role="img" aria-label="Brand growth motif in white outline"></div>
  </section>

  <section class="card card-back">
    <div class="holder">
      <p class="name">Lorem Ipsum Dolor</p>
      <p class="role">Public Relations</p>
      <p class="contact">(421) 555.0192<br>12 Harrow Lane London<br>media@kt7staffing-example.com<br>www.kt7staffing-example.com</p>
    </div>
    <div class="wordmark"><span class="mark-square"></span>KT7 Staffing</div>
    <div class="growth-corner" role="img" aria-label="Brand growth motif in light grey outline"></div>
  </section>
</body>
</html>
```